Financial advisory firm needs new business card design

Business card design , simple , elegant, professional. Will use existing logo. One side should be a solid blue background (matching blue in Logo) . info side should have basic info, maybe two color panes. one white, one a different color..maybe light grey. Please visit our website to get feel for colors and business. www.tallowmeadwealth.com

Industry/Entity Type

Financial Service

Contact Information for Business Card

Basic info..minimalist, modern, approach

Colors

Designer to choose colors to be used in the design.

Requirements
Must have
• Important regulatory requirement. The following disclosure MUST be included somewhere on the business card. It can be either front, or back, and it may be in a smaller font (but has to be legible). My interest is to satisfy the requirement with the least possible disruption to the beauty of the card design.
• All securities offered through the Harrowgate Capital, Inc. Oakhurst Lane, NJ. Member QOLTA/DWEM. Advisory services provided through HC Advisory Services, Inc. an PBR Registered Investment Advisor.

```html
<!DOCTYPE html>
<html lang="en">
<head>
<meta charset="utf-8">
<title>Tallowmead Wealth – Business Card</title>
<link rel="stylesheet" href="https://fonts.googleapis.com/css2?family=Open+Sans:wght@400;600&display=swap">
<style>
  :root {
    --stage: #d9dadc;
    --brand-blue: #084a86;
    --accent-blue: #1a74c4;
    --card-white: #f1f1f1;
    --card-dark: #222124;
    --ink: #1b1b1d;
    --paper-text: #ffffff;
    --fine-print: rgba(255,255,255,0.82);
  }
  * { box-sizing: border-box; margin: 0; padding: 0; }
  html, body { width: 1200px; height: 1021px; overflow: hidden; }
  body {
    background: var(--stage);
    font-family: "Open Sans", sans-serif;
    position: relative;
  }
  .card {
    position: absolute;
    left: 230px;
    width: 740px;
    height: 423px;
    overflow: hidden;
    box-shadow: 0 6px 18px rgba(0,0,0,0.18);
  }
  .card--back { top: 50px; background: var(--brand-blue); }
  .card--front { top: 548px; background: var(--card-dark); }

  .wordmark {
    position: absolute;
    display: flex;
    align-items: center;
    gap: 14px;
    font-weight: 600;
    letter-spacing: 0.04em;
    text-transform: uppercase;
    white-space: nowrap;
  }
  .wordmark__dot { width: 16px; height: 16px; border-radius: 50%; }
  .card--back .wordmark {
    left: 0; right: 0; top: 130px; justify-content: center;
    font-size: 42px; color: var(--paper-text);
  }
  .card--back .wordmark__dot { background: var(--paper-text); }
  .back-url {
    position: absolute; left: 0; right: 0; top: 292px;
    text-align: center; color: var(--paper-text);
    font-size: 17px; letter-spacing: 0.12em;
  }
  .disclosure {
    position: absolute; left: 60px; right: 60px; bottom: 26px;
    text-align: center; color: var(--fine-print);
    font-size: 11px; line-height: 1.5;
  }

  .front-top {
    position: absolute; left: 0; top: 0; width: 100%; height: 220px;
    background: linear-gradient(90deg, #ffffff, var(--card-white));
    border-bottom: 5px solid var(--accent-blue);
  }
  .card--front .wordmark {
    left: 0; right: 0; top: 82px; justify-content: center;
    font-size: 44px; color: var(--ink);
  }
  .card--front .wordmark__dot { background: var(--ink); }
  .notch { position: absolute; left: 140px; top: 224px; }
  .holder { position: absolute; left: 70px; top: 268px; }
  .holder__name { color: var(--accent-blue); font-weight: 600; font-size: 24px; }
  .holder__role { color: var(--paper-text); font-size: 18px; margin-top: 2px; }
  .contact {
    position: absolute; left: 418px; top: 262px;
    color: var(--paper-text); font-size: 17px; line-height: 1.45;
    list-style: none;
  }
  .contact li { display: flex; align-items: center; gap: 10px; }
  .contact .address { padding-left: 26px; }
  .contact svg { width: 16px; height: 16px; flex: none; }
</style>
</head>
<body>

<section class="card card--back" aria-label="Card back">
  <div class="wordmark"><span class="wordmark__dot"></span>Tallowmead Wealth</div>
  <p class="back-url">www.tallowmeadwealth.com</p>
  <p class="disclosure">All securities offered through Harrowgate Capital, Inc. Oakhurst Lane, NJ. Member QOLTA/DWEM. Advisory services provided through HC Advisory Services, Inc. a PBR Registered Investment Advisor.</p>
</section>

<section class="card card--front" aria-label="Card front">
  <div class="front-top"></div>
  <div class="wordmark"><span class="wordmark__dot"></span>Tallowmead Wealth</div>
  <svg class="notch" width="30" height="14" viewBox="0 0 30 14"><polygon points="0,0 30,0 15,14" fill="var(--accent-blue)"/></svg>

  <div class="holder">
    <p class="holder__name">Daniel Osterby</p>
    <p class="holder__role">President &amp; Founder</p>
  </div>

  <ul class="contact">
    <li class="address">48 Fernbrook Road, Suite 110</li>
    <li class="address">Linwood, NJ 07412</li>
    <li>
      <svg viewBox="0 0 16 16" aria-hidden="true"><path d="M3 1.5l3 .5 1 3.5-1.8 1.2a9 9 0 0 0 4.1 4.1L10.5 9l3.5 1 .5 3-2 1.5C6.5 14 2 9.5 1.5 3.5z" fill="var(--accent-blue)"/></svg>
      (555) 214-6390
    </li>
    <li>
      <svg viewBox="0 0 16 16" aria-hidden="true"><rect x="1" y="3" width="14" height="10" fill="none" stroke="var(--accent-blue)" stroke-width="1.5"/><path d="M1 3l7 6 7-6" fill="none" stroke="var(--accent-blue)" stroke-width="1.5"/></svg>
      info@tallowmeadwealth.com
    </li>
    <li>
      <svg viewBox="0 0 16 16" aria-hidden="true"><g fill="none" stroke="var(--accent-blue)" stroke-width="1.3"><circle cx="8" cy="8" r="6.5"/><ellipse cx="8" cy="8" rx="3" ry="6.5"/><path d="M1.5 8h13"/></g></svg>
      www.tallowmeadwealth.com
    </li>
  </ul>
</section>

</body>
</html>
```